Lumo4Kart - a fintech company - business card

We need a business card design for our Payments Technology company in Sydney, Australia. We provide business with payment solutions expanding across EFTPOS machines, online payment gateways and mobile payment solutions. We would like to see designs that are clean, classy and professional.
Target Market(s)
Business professionals, executives, c-suite
Industry/Entity Type
Fintech
Contact Information for Business Card
Will be on 400gsm. Logo will most likely be spot gloss unless designer recommends otherwise.
Font styles to use
Sans Serif
Requirements
Must have
- We need our website (lumo4kart.com.au), email (contact@lumo4kart.com.au), mobile (0432 587 904) and direct phone number (02 6815 3927) to feature on the card along with our logo (attached) and the words "EFTPOS | ONLINE | MOBILE"
- Font = Roboto

```html
<!DOCTYPE html>
<html lang="en">
<head>
<meta charset="utf-8">
<title>Lumo4Kart Business Card</title>
<link rel="stylesheet" href="https://fonts.googleapis.com/css2?family=Roboto:wght@400;500;700&display=swap">
<style>
  :root{
    --stage:#2b2b2d;
    --paper:#ffffff;
    --brand-blue:#145f96;
    --ribbon:#6d6e71;
    --ribbon-fold:#4a4b4d;
    --ink:#1e1e1e;
  }
  *{margin:0;padding:0;box-sizing:border-box}
  html,body{width:1200px;height:900px;overflow:hidden}
  body{background:var(--stage);font-family:"Roboto",sans-serif;position:relative}
  .card{position:absolute;width:560px;height:320px;background:var(--paper);border-radius:18px;overflow:hidden;box-shadow:0 14px 30px rgba(0,0,0,.45)}
  .card--back{left:90px;top:100px}
  .card--front{left:550px;top:480px}

  /* back */
  .back-name{position:absolute;left:0;right:0;top:108px;text-align:center;font-weight:500;font-size:46px;color:var(--ink);letter-spacing:.5px}
  .tagline{position:absolute;left:0;right:0;top:220px;text-align:center;font-size:15px;color:var(--ink);letter-spacing:1px}

  /* front */
  .front-shapes{position:absolute;inset:0}
  .front-name{position:absolute;left:36px;top:112px;font-weight:500;font-size:28px;color:var(--ink);letter-spacing:.3px}
  .person{position:absolute;left:268px;top:36px;width:210px;color:#fff}
  .person__name{font-weight:700;font-size:17px;letter-spacing:.5px;text-transform:uppercase}
  .person__role{font-size:10px;margin-top:2px}
  .contacts{position:absolute;left:36px;top:190px;list-style:none}
  .contacts li{display:flex;align-items:center;gap:10px;height:24px;font-size:13px;color:var(--ink)}
  .contacts svg{width:18px;height:18px;flex:none}
  .address{position:absolute;left:380px;top:212px;width:170px;text-align:center;color:#fff;font-size:12px;line-height:1.4}
  .address svg{display:block;margin:0 auto 6px;width:12px;height:16px}
</style>
</head>
<body>

<section class="card card--back" aria-label="Card back">
  <p class="back-name">Lumo4Kart</p>
  <p class="tagline">" EFTPOS | ONLINE | MOBILE"</p>
</section>

<section class="card card--front" aria-label="Card front">
  <svg class="front-shapes" viewBox="0 0 560 320" width="560" height="320" aria-hidden="true">
    <defs>
      <filter id="edge-shadow" x="-10%" y="-10%" width="120%" height="120%">
        <feDropShadow dx="-3" dy="0" stdDeviation="4" flood-opacity=".3"/>
      </filter>
    </defs>
    <polygon points="262,0 560,0 560,320 340,320" fill="var(--brand-blue)" filter="url(#edge-shadow)"/>
    <polygon points="248,88 270,88 270,102" fill="var(--ribbon-fold)"/>
    <rect x="248" y="28" width="250" height="60" fill="var(--ribbon)"/>
  </svg>

  <p class="front-name">Lumo4Kart</p>

  <div class="person">
    <p class="person__name">Daniel Reyes</p>
    <p class="person__role">Founder &amp; Director</p>
  </div>

  <ul class="contacts">
    <li>
      <svg viewBox="0 0 18 18"><rect width="18" height="18" fill="var(--brand-blue)"/><path d="M5 4l2 0 1 3-1.5 1a7 7 0 0 0 3.5 3.5l1-1.5 3 1v2a1 1 0 0 1-1 1A9 9 0 0 1 4 5a1 1 0 0 1 1-1z" fill="#fff"/></svg>
      0432 587 904
    </li>
    <li>
      <svg viewBox="0 0 18 18"><rect width="18" height="18" fill="var(--brand-blue)"/><rect x="4" y="8" width="10" height="6" rx="1" fill="#fff"/><path d="M3 7c2-3 10-3 12 0v1h-3V7H6v1H3z" fill="#fff"/></svg>
      02 6815 3927
    </li>
    <li>
      <svg viewBox="0 0 18 18"><rect width="18" height="18" fill="var(--brand-blue)"/><rect x="3.5" y="5" width="11" height="8" fill="none" stroke="#fff" stroke-width="1.2"/><path d="M3.5 5l5.5 4.5L14.5 5" fill="none" stroke="#fff" stroke-width="1.2"/></svg>
      contact@lumo4kart.com.au
    </li>
    <li>
      <svg viewBox="0 0 18 18"><rect width="18" height="18" fill="var(--brand-blue)"/><circle cx="9" cy="9" r="5" fill="none" stroke="#fff" stroke-width="1.2"/><path d="M4 9h10M9 4c-2.5 3-2.5 7 0 10M9 4c2.5 3 2.5 7 0 10" fill="none" stroke="#fff" stroke-width="1"/></svg>
      lumo4kart.com.au
    </li>
  </ul>

  <div class="address">
    <svg viewBox="0 0 12 16"><path d="M6 0a6 6 0 0 1 6 6c0 4-6 10-6 10S0 10 0 6a6 6 0 0 1 6-6z" fill="#fff"/><circle cx="6" cy="6" r="2.2" fill="var(--brand-blue)"/></svg>
    48 Harbour Lane - Pyrmont<br>NSW 2009
  </div>
</section>

</body>
</html>
```